Rehab/fitness Business card design

I need a design that promotes "A ready made base for runners". services include assessment, massage, physiotherapy, pilates, suspension training, kinesiotaping in any combination.
I would like to bring the design into my website, flyers etc

Target Market(s)

athletes from beginner to elite - any age, male and female

Industry/Entity Type

Shop

Contact Information for Business Card

Ready-Made-Base for Runners
17 Parvel Crescent, Hollowmere, Wrenhaven
021 847 3610
gwen.farrowby@quillmail.test

Logo Text

Requirements
Nice to have
• Blue colour theme

```html
<!DOCTYPE html>
<html lang="en">
<head>
<meta charset="utf-8">
<title>Ready-Made-Base for Runners — Business Card</title>
<link href="https://fonts.googleapis.com/css2?family=Michroma&family=Fira+Sans+Condensed:wght@400;600&display=swap" rel="stylesheet">
<style>
  :root {
    --page-bg: #e8e6e3;
    --card-border: #ffffff;
    --card-glow: #34479b;
    --card-edge: #1e2264;
    --headline: #d3dcf3;
    --name: #b8c6ef;
    --label: #a6b4e4;
    --text: #ffffff;
    --rule: #ffffff;
  }
  * { margin: 0; padding: 0; box-sizing: border-box; }
  html, body { width: 1200px; height: 1181px; overflow: hidden; }
  body { background: var(--page-bg); position: relative; font-family: "Fira Sans Condensed", Arial, sans-serif; }

  .card {
    position: absolute;
    left: 233px;
    width: 734px;
    border: 9px solid var(--card-border);
    background: radial-gradient(ellipse 60% 65% at 50% 45%, var(--card-glow) 0%, #2a3482 45%, var(--card-edge) 100%);
    box-shadow: 0 6px 18px rgba(0,0,0,0.25);
    color: var(--text);
  }
  .card--front { top: 131px; height: 422px; }
  .card--back  { top: 618px; height: 422px; }

  .headline {
    position: absolute; left: 0; right: 0; top: 186px;
    text-align: center;
    font-family: "Michroma", Arial, sans-serif;
    font-size: 20px; letter-spacing: 0.3px;
    color: var(--headline);
    text-shadow: 0 1px 2px rgba(0,0,0,0.5);
  }

  .services {
    position: absolute; left: 183px; width: 352px; top: 329px;
    text-align: center; font-size: 14.5px; line-height: 17.5px;
  }
  .services__title { color: var(--label); font-size: 15px; letter-spacing: 0.6px; margin-bottom: 1px; }
  .services__list {
    border-left: 3px solid var(--rule); border-right: 3px solid var(--rule);
    padding: 6px 4px 0; margin-top: -6px; height: 42px;
  }

  .identity {
    position: absolute; right: 386px; top: 180px; text-align: right;
  }
  .identity__name { font-weight: 600; font-size: 31px; line-height: 29px; letter-spacing: 1.6px; color: var(--name); }
  .identity__role { font-size: 15.5px; letter-spacing: 1.9px; line-height: 16px; }

  .divider { position: absolute; left: 357px; top: 141px; width: 3px; height: 122px; background: var(--rule); }

  .contact { position: absolute; left: 386px; top: 160px; font-size: 15px; line-height: 17px; }
  .contact dt { color: var(--label); display: inline; }
  .contact dd { display: inline; }
  .contact .row { display: block; }
</style>
</head>
<body>
  <section class="card card--front">
    <h1 class="headline">READY-MADE-BASE FOR RUNNERS</h1>
    <div class="services">
      <p class="services__title">SERVICES WE OFFER</p>
      <p class="services__list">Assessment - Massage - Physiotherapy - Pilates -<br>Suspension training - Kinesiotaping in any combination.</p>
    </div>
  </section>

  <section class="card card--back">
    <div class="identity">
      <p class="identity__name">YOUR NAME</p>
      <p class="identity__role">MANAGING DIRECTOR</p>
    </div>
    <div class="divider"></div>
    <dl class="contact">
      <div class="row"><dt>Web&nbsp;&nbsp;&nbsp;: </dt><dd>www.website.com</dd></div>
      <div class="row"><dt>Email : </dt><dd>gwen.farrowby@quillmail.test</dd></div>
      <div class="row"><dt>Phone : </dt><dd>021 847 3610</dd></div>
      <div class="row"><dd>17 Parvel Crescent, Hollowmere,</dd></div>
      <div class="row"><dd>Wrenhaven</dd></div>
    </dl>
  </section>
</body>
</html>
```